Business Card Design for electrician

The name of the company is: Harbour Stone Electrical (electrical contractors)

we are a small electrical business who service residential and light commercial businesses.

I want the design to represent a subtle eco friendly image as well as being professional

A green colour should be used somewhere in the design
Hi

I do not have a logo but a nice font for the business name will do fine.

Here is the information that will need to go on the card:

Dorian Finch
Manager

Ph: 09 4817263
Mob: 02107436158
Residential and commercial installations and maintenance

Target Market(s)

Home owner or small business owner

Industry/Entity Type

Electrician

Requirements
Should not have
• should not have cheesy clip art images of power sockets or lightning bolts etc

```html
<!DOCTYPE html>
<html lang="en">
<head>
<meta charset="utf-8">
<title>Harbour Stone Electrical – Business Card</title>
<link rel="stylesheet" href="https://fonts.googleapis.com/css2?family=Encode+Sans+Condensed:wght@300;400&display=swap">
<style>
  :root {
    --page: #ffffff;
    --card: #000000;
    --ink: #ffffff;
    --leaf: #5c9c4f;
    --rule: #bfbfbf;
  }
  * { margin: 0; padding: 0; box-sizing: border-box; }
  html, body {
    width: 848px;
    height: 1200px;
    overflow: hidden;
    background: var(--page);
  }
  .page {
    position: relative;
    width: 848px;
    height: 1200px;
  }
  .business-card {
    position: absolute;
    left: 225px;
    top: 311px;
    width: 369px;
    height: 229px;
    background: var(--card);
    color: var(--ink);
    font-family: "Encode Sans Condensed", "Arial Narrow", sans-serif;
    font-weight: 300;
  }
  .services {
    position: absolute;
    left: 21px;
    right: 24px;
    top: 10px;
    display: flex;
    justify-content: space-between;
    align-items: center;
    font-size: 13px;
    letter-spacing: 0.1px;
    list-style: none;
  }
  .services .bullet {
    width: 5px;
    height: 5px;
    border-radius: 50%;
    background: var(--leaf);
  }
  .company-name {
    position: absolute;
    left: 0;
    right: 0;
    top: 80px;
    text-align: center;
    font-size: 36px;
    font-weight: 300;
    letter-spacing: -0.6px;
    line-height: 1;
    white-space: nowrap;
  }
  .contact {
    position: absolute;
    right: 24px;
    top: 184px;
    display: grid;
    grid-template-columns: auto auto;
    column-gap: 5px;
    row-gap: 1px;
    align-items: baseline;
    line-height: 1.1;
  }
  .contact .person {
    text-align: right;
    padding-right: 5px;
    border-right: 1px solid var(--rule);
  }
  .contact .person-name { font-size: 11px; }
  .contact .person-role { font-size: 17px; letter-spacing: -0.2px; }
  .contact .phone { font-size: 14px; }
  .contact .mobile { font-size: 10.5px; }
</style>
</head>
<body>
  <main class="page">
    <section class="business-card">
      <ul class="services">
        <li>Residential</li>
        <li class="bullet" aria-hidden="true"></li>
        <li>Commercial</li>
        <li class="bullet" aria-hidden="true"></li>
        <li>Installations</li>
        <li class="bullet" aria-hidden="true"></li>
        <li>Maintenance</li>
      </ul>

      <h1 class="company-name">Harbour Stone Electrical</h1>

      <div class="contact">
        <span class="person person-name">Dorian Finch</span>
        <span class="phone">Ph: 09 4817263</span>
        <span class="person person-role">Manager</span>
        <span class="mobile">Mob: 02107436158</span>
      </div>
    </section>
  </main>
</body>
</html>
```